Daily, Weekly, Monthly Client & Prospect Tracker

I am a financial advisor looking for a spreadsheet that allows me to track my daily, weekly, and monthly activites & contact with clients and the same for prospects with the attached categories. I'd like to have all of the individual sheets feed data into the next (i.e daily adds to weekly and so on). I'd also like a sheet with a total list for the day, week, month, year. I'd also like an area to leave notes. Another feature is the ability to track prospecting, lead, and client sales stage. I've had a very difficult time creating a spreadsheet that encompasses all of these features. I currently have 10 different spreadsheets. I would prefer if there are also sheets that copy information and input it into a sheet specific for the bulk lead import format for Salesforce. As a side note, I have ADHD and looking for a esthetically pleasing color coordinated document so that I stay organized. Let me know your thoughts.

```html
<!DOCTYPE html>
<html lang="en">
<head>
<meta charset="utf-8">
<title>Daily, Weekly, Monthly Client &amp; Prospect Tracker</title>
<link rel="stylesheet" href="https://fonts.googleapis.com/css2?family=Arimo:wght@400;700&display=swap">
<style>
  :root {
    --paper: #ffffff;
    --ink: #000000;
    --grid: #d4d7dc;
    --chrome: #eef0f3;
    --chrome-edge: #c3c8cf;
    --chrome-text: #3b3b3b;
    --header-fill: #4a4428;
    --header-text: #ffffff;
    --title-fill: #000000;
    --title-text: #ffffff;
  }
  * { box-sizing: border-box; margin: 0; padding: 0; }
  html, body { width: 1200px; height: 406px; overflow: hidden; background: var(--paper); }
  body { font-family: "Arimo", Arial, sans-serif; }

  .sheet {
    width: 1200px;
    height: 406px;
    overflow: hidden;
    position: relative;
  }
  .tracker {
    border-collapse: collapse;
    table-layout: fixed;
    width: 1200px;
  }
  .tracker td, .tracker th {
    border: 1px solid var(--grid);
    padding: 0;
    overflow: hidden;
    white-space: nowrap;
  }

  /* spreadsheet chrome */
  .col-letters th {
    height: 11px;
    background: linear-gradient(var(--paper), var(--chrome));
    border-color: var(--chrome-edge);
    color: var(--chrome-text);
    font-weight: 400;
    font-size: 9px;
    line-height: 10px;
    text-align: center;
  }
  .row-num {
    background: var(--chrome);
    border-color: var(--chrome-edge) !important;
    color: var(--chrome-text);
    font-size: 9px;
    font-weight: 400;
    text-align: center;
  }

  /* title band */
  .row-top-a { height: 15px; }
  .row-top-b { height: 25px; }
  .title-band {
    background: var(--title-fill);
    color: var(--title-text);
    font-size: 25px;
    font-weight: 700;
    text-align: center;
    vertical-align: middle;
    letter-spacing: 0.2px;
    border: 1px solid var(--title-fill) !important;
  }

  /* table header */
  .field-row { height: 36px; }
  .field-row .field {
    background: var(--header-fill);
    color: var(--header-text);
    font-size: 10.5px;
    font-weight: 700;
    text-align: center;
    vertical-align: middle;
    border: 3px solid var(--ink);
  }

  /* entry rows */
  .entry { height: 18.5px; }
  .entry .cell {
    border: 2.5px solid var(--ink);
    font-size: 12px;
    font-weight: 700;
    color: var(--ink);
    vertical-align: middle;
    line-height: 13px;
  }
  .cell.date, .cell.money { text-align: center; }
  .cell.phone { text-align: left; padding-left: 2px; }
</style>
</head>
<body>
<div class="sheet">
  <table class="tracker">
    <colgroup>
      <col style="width:20px">
      <col style="width:107px">
      <col style="width:95px">
      <col style="width:89px">
      <col style="width:88px">
      <col style="width:97px">
      <col style="width:109px">
      <col style="width:96px">
      <col style="width:70px">
      <col style="width:78px">
      <col style="width:71px">
      <col style="width:74px">
      <col style="width:67px">
      <col style="width:139px">
    </colgroup>
    <tr class="col-letters">
      <th></th><th>A</th><th>B</th><th>C</th><th>D</th><th>E</th><th>F</th><th>G</th><th>H</th><th>I</th><th>J</th><th>K</th><th>L</th><th>M</th>
    </tr>
    <tr class="row-top-a">
      <td class="row-num">1</td><td></td><td></td>
      <td class="title-band" colspan="9" rowspan="2">Daily,Weekly,Monthly Client &amp;Prospect Tracker</td>
      <td></td><td></td>
    </tr>
    <tr class="row-top-b">
      <td class="row-num">2</td><td></td><td></td><td></td><td></td>
    </tr>
    <tr class="field-row">
      <td class="row-num">3</td>
      <th class="field">The Date</th>
      <th class="field">Advisor Name</th>
      <th class="field">Contact</th>
      <th class="field">State</th>
      <th class="field">Product Name</th>
      <th class="field">Total Assets($)</th>
      <th class="field">T12 Revenue($)</th>
      <th class="field">total day</th>
      <th class="field">Total Week</th>
      <th class="field">Total Month</th>
      <th class="field">Total Year</th>
      <th class="field">The Total</th>
      <th class="field">Notes</th>
    </tr>
    <tr class="entry"><td class="row-num">4</td><td class="cell date">04-02-2023</td><td class="cell"></td><td class="cell phone">(+1)</td><td class="cell"></td><td class="cell"></td><td class="cell money">$</td><td class="cell money">$</td><td class="cell"></td><td class="cell"></td><td class="cell"></td><td class="cell"></td><td class="cell"></td><td class="cell"></td></tr>
    <tr class="entry"><td class="row-num">5</td><td class="cell date">05-02-2023</td><td class="cell"></td><td class="cell phone">(+1)</td><td class="cell"></td><td class="cell"></td><td class="cell money">$</td><td class="cell money">$</td><td class="cell"></td><td class="cell"></td><td class="cell"></td><td class="cell"></td><td class="cell"></td><td class="cell"></td></tr>
    <tr class="entry"><td class="row-num">6</td><td class="cell date">06-02-2023</td><td class="cell"></td><td class="cell phone">(+1)</td><td class="cell"></td><td class="cell"></td><td class="cell money">$</td><td class="cell money">$</td><td class="cell"></td><td class="cell"></td><td class="cell"></td><td class="cell"></td><td class="cell"></td><td class="cell"></td></tr>
    <tr class="entry"><td class="row-num">7</td><td class="cell date">07-02-2023</td><td class="cell"></td><td class="cell phone">(+1)</td><td class="cell"></td><td class="cell"></td><td class="cell money">$</td><td class="cell money">$</td><td class="cell"></td><td class="cell"></td><td class="cell"></td><td class="cell"></td><td class="cell"></td><td class="cell"></td></tr>
    <tr class="entry"><td class="row-num">8</td><td class="cell date">08-02-2023</td><td class="cell"></td><td class="cell phone">(+1)</td><td class="cell"></td><td class="cell"></td><td class="cell money">$</td><td class="cell money">$</td><td class="cell"></td><td class="cell"></td><td class="cell"></td><td class="cell"></td><td class="cell"></td><td class="cell"></td></tr>
    <tr class="entry"><td class="row-num">9</td><td class="cell date">09-02-2023</td><td class="cell"></td><td class="cell phone">(+1)</td><td class="cell"></td><td class="cell"></td><td class="cell money">$</td><td class="cell money">$</td><td class="cell"></td><td class="cell"></td><td class="cell"></td><td class="cell"></td><td class="cell"></td><td class="cell"></td></tr>
    <tr class="entry"><td class="row-num">10</td><td class="cell date">10-02-2023</td><td class="cell"></td><td class="cell phone">(+1)</td><td class="cell"></td><td class="cell"></td><td class="cell money">$</td><td class="cell money">$</td><td class="cell"></td><td class="cell"></td><td class="cell"></td><td class="cell"></td><td class="cell"></td><td class="cell"></td></tr>
    <tr class="entry"><td class="row-num">11</td><td class="cell date">11-02-2023</td><td class="cell"></td><td class="cell phone">(+1)</td><td class="cell"></td><td class="cell"></td><td class="cell money">$</td><td class="cell money">$</td><td class="cell"></td><td class="cell"></td><td class="cell"></td><td class="cell"></td><td class="cell"></td><td class="cell"></td></tr>
    <tr class="entry"><td class="row-num">12</td><td class="cell date">12-02-2023</td><td class="cell"></td><td class="cell phone">(+1)</td><td class="cell"></td><td class="cell"></td><td class="cell money">$</td><td class="cell money">$</td><td class="cell"></td><td class="cell"></td><td class="cell"></td><td class="cell"></td><td class="cell"></td><td class="cell"></td></tr>
    <tr class="entry"><td class="row-num">13</td><td class="cell date">13-02-2023</td><td class="cell"></td><td class="cell phone">(+1)</td><td class="cell"></td><td class="cell"></td><td class="cell money">$</td><td class="cell money">$</td><td class="cell"></td><td class="cell"></td><td class="cell"></td><td class="cell"></td><td class="cell"></td><td class="cell"></td></tr>
    <tr class="entry"><td class="row-num">14</td><td class="cell date">14-02-2023</td><td class="cell"></td><td class="cell phone">(+1)</td><td class="cell"></td><td class="cell"></td><td class="cell money">$</td><td class="cell money">$</td><td class="cell"></td><td class="cell"></td><td class="cell"></td><td class="cell"></td><td class="cell"></td><td class="cell"></td></tr>
    <tr class="entry"><td class="row-num">15</td><td class="cell date">15-02-2023</td><td class="cell"></td><td class="cell phone">(+1)</td><td class="cell"></td><td class="cell"></td><td class="cell money">$</td><td class="cell money">$</td><td class="cell"></td><td class="cell"></td><td class="cell"></td><td class="cell"></td><td class="cell"></td><td class="cell"></td></tr>
    <tr class="entry"><td class="row-num">16</td><td class="cell date">16-02-2023</td><td class="cell"></td><td class="cell phone">(+1)</td><td class="cell"></td><td class="cell"></td><td class="cell money">$</td><td class="cell money">$</td><td class="cell"></td><td class="cell"></td><td class="cell"></td><td class="cell"></td><td class="cell"></td><td class="cell"></td></tr>
    <tr class="entry"><td class="row-num">17</td><td class="cell date">17-02-2023</td><td class="cell"></td><td class="cell phone">(+1)</td><td class="cell"></td><td class="cell"></td><td class="cell money">$</td><td class="cell money">$</td><td class="cell"></td><td class="cell"></td><td class="cell"></td><td class="cell"></td><td class="cell"></td><td class="cell"></td></tr>
    <tr class="entry"><td class="row-num">18</td><td class="cell date">18-02-2023</td><td class="cell"></td><td class="cell phone">(+1)</td><td class="cell"></td><td class="cell"></td><td class="cell money">$</td><td class="cell money">$</td><td class="cell"></td><td class="cell"></td><td class="cell"></td><td class="cell"></td><td class="cell"></td><td class="cell"></td></tr>
    <tr class="entry"><td class="row-num">19</td><td class="cell date">19-02-2023</td><td class="cell"></td><td class="cell phone">(+1)</td><td class="cell"></td><td class="cell"></td><td class="cell money">$</td><td class="cell money">$</td><td class="cell"></td><td class="cell"></td><td class="cell"></td><td class="cell"></td><td class="cell"></td><td class="cell"></td></tr>
    <tr class="entry"><td class="row-num">20</td><td class="cell date">20-02-2023</td><td class="cell"></td><td class="cell phone">(+1)</td><td class="cell"></td><td class="cell"></td><td class="cell money">$</td><td class="cell money">$</td><td class="cell"></td><td class="cell"></td><td class="cell"></td><td class="cell"></td><td class="cell"></td><td class="cell"></td></tr>
  </table>
</div>
</body>
</html>
```